Brightway Haul & Repair Services, are a company that offers a 'one stop shop' pre-move clean up a

I have already selected a logo which I would like on the front of the business cards along with phone numbers, web address and email which are:
0419574302
www.brightwayhaul.com.au
brightwayhaulrepair@mailbox.example

On the back of the card I would like to list some of the types of service we offer (clean - move - repairs/maintenance) which are:
CLEAN - windows, gutters, solar panels, driveways/paths, carpets.
MOVE - Small/medium size house/office moves, large item pick-up & delivery, yard clean-up and removal.
General maintenance and repairs.

I would like the blue logo on a gray background.

Thanks

```html
<!DOCTYPE html>
<html lang="en">
<head>
<meta charset="utf-8">
<title>Brightway Haul &amp; Repair Services – Business Card</title>
<link rel="stylesheet" href="https://fonts.googleapis.com/css2?family=Arimo:wght@700&family=Caladea:ital,wght@0,400;0,700;1,400&display=swap">
<style>
  :root {
    --page-bg: #ece8e2;
    --card-grey: #c9c9c8;
    --card-light: #dededd;
    --brand-blue: #2f56a4;
    --text-white: #ffffff;
  }
  * { margin: 0; padding: 0; box-sizing: border-box; }
  html, body {
    width: 900px;
    height: 1200px;
    overflow: hidden;
    background: var(--page-bg);
  }
  .card {
    position: absolute;
    background: var(--card-grey);
    overflow: hidden;
  }
  .card-front { left: 50px; top: 125px; width: 790px; height: 450px; }
  .card-back  { left: 50px; top: 622px; width: 793px; height: 451px; }
  .card-sheen {
    position: absolute;
    inset: 0;
    width: 100%;
    height: 100%;
  }
  .card-sheen polygon { fill: var(--card-light); }

  .contact-list {
    position: absolute;
    left: 28px;
    top: 38px;
    list-style: none;
    font-family: "Caladea", serif;
    font-size: 23px;
    line-height: 32px;
    color: var(--text-white);
  }
  .contact-list li::before {
    content: "\27A5";
    font-size: 15px;
    margin-right: 12px;
    vertical-align: 3px;
  }
  .contact-web { font-weight: 700; }

  .brand-name {
    position: absolute;
    font-family: "Arimo", sans-serif;
    font-weight: 700;
    color: var(--brand-blue);
    text-transform: uppercase;
    text-align: center;
  }
  .card-front .brand-name {
    left: 55px;
    top: 205px;
    width: 700px;
    font-size: 62px;
    line-height: 70px;
  }
  .card-back .brand-name {
    left: 368px;
    top: 50px;
    width: 390px;
    font-size: 33px;
    line-height: 40px;
  }

  .service-list {
    position: absolute;
    left: 19px;
    top: 20px;
    font-family: "Caladea", serif;
    font-style: italic;
    font-size: 18px;
    line-height: 25.6px;
    color: var(--text-white);
  }
  .service-group + .service-group { margin-top: 25.6px; }

  .service-summary {
    position: absolute;
    right: 52px;
    top: 252px;
    list-style: none;
    text-align: right;
    font-family: "Arimo", sans-serif;
    font-weight: 700;
    font-size: 29px;
    line-height: 44.5px;
    color: var(--brand-blue);
  }
</style>
</head>
<body>

<section class="card card-front" aria-label="Card front">
  <svg class="card-sheen" viewBox="0 0 790 450" preserveAspectRatio="none" aria-hidden="true">
    <polygon points="735,0 790,0 790,450 475,450"/>
  </svg>
  <ul class="contact-list">
    <li class="contact-web">www.brightwayhaul.com.au</li>
    <li>brightwayhaulrepair@mailbox.example</li>
    <li>tel: 0419574302</li>
  </ul>
  <p class="brand-name">Brightway Haul<br>&amp; Repair Services</p>
</section>

<section class="card card-back" aria-label="Card back">
  <svg class="card-sheen" viewBox="0 0 793 451" preserveAspectRatio="none" aria-hidden="true">
    <polygon points="720,0 793,0 793,451 380,451"/>
  </svg>
  <div class="service-list">
    <p class="service-group">CLEAN<br>windows<br>gutters<br>solar panels<br>driveways/paths<br>carpets</p>
    <p class="service-group">MOVE<br>Small/medium size house/office moves<br>large item pick-up &amp; delivery<br>yard clean-up and removal</p>
    <p class="service-group">General<br>MAINTENANCE &amp; REPAIRS</p>
  </div>
  <p class="brand-name">Brightway Haul<br>&amp; Repair Services</p>
  <ul class="service-summary">
    <li>CLEAN</li>
    <li>MOVE</li>
    <li>REPAIR</li>
    <li>MAINTENANCE</li>
  </ul>
</section>

</body>
</html>
```